Harbor Lantern Productions Business Logo and Card Design

PLEASE LIMIT your submission to maximum of 2 at a time.
Harbor Lantern Productions provides video production services, and produces videos, that help people connect in the spirit of unity and peace.Primarily I am looking for a logo that is simple to remember but the concept is fairly complex. The concept of the logo is a peace dove with an olive branch in it's mouth has it's wings around earth, symbolising that it is protecting earth with peace. If possible I'd like this logo done and delivered in high quality vector format, so I can use it for banners etc.Then the business card I just want a simple white card with the logo in the middle and contact info under the logo. Open to suggestions if you think there should be anything else included, but it must remain simple and uncluttered. Also incorporate something in the logo that says film and video e.g.: film strip or camera lens

Contact Information for Business Card

Harbor Lantern Productions
www.harborlantern.example
teodor@harborlantern.example
+61 478 315 064

Requirements
Must have
• Logo must have the following:
• Peace Dove
• Olive branch
• Earth
• Something about video production (e.g.: film strip or camera lens or anything film related)

```html
<!DOCTYPE html>
<html lang="en">
<head>
<meta charset="utf-8">
<title>Harbor Lantern Productions – Business Card</title>
<link rel="stylesheet" href="https://fonts.googleapis.com/css2?family=Roboto+Condensed:wght@400;700&display=swap">
<style>
  :root {
    --stage: #e9e6e1;
    --card: #ffffff;
    --card-shade: #e4e6e8;
    --ink: #1f7db1;
    --ink-soft: #9cc3d9;
  }
  * { box-sizing: border-box; margin: 0; padding: 0; }
  html, body {
    width: 1200px; height: 892px; overflow: hidden;
    background: var(--stage);
    font-family: "Roboto Condensed", Arial, sans-serif;
  }
  .canvas {
    position: relative; width: 1200px; height: 892px;
    display: flex; align-items: center; justify-content: center;
  }
  .business-card {
    position: relative;
    width: 980px; height: 560px;
    background: linear-gradient(135deg, var(--card) 0%, var(--card) 45%, var(--card-shade) 100%);
    box-shadow: 0 14px 40px rgba(0,0,0,.18);
    display: flex;
    color: var(--ink);
  }
  .brand-side {
    width: 490px; height: 100%;
    display: flex; flex-direction: column; align-items: center; justify-content: center;
    gap: 28px;
  }
  .logo-artwork {
    width: 280px; height: 230px; border-radius: 50%;
    background: radial-gradient(circle at 50% 45%, #eaf2f7 0%, #cfe1ec 70%, #b7d2e3 100%);
  }
  .brand-name {
    font-weight: 700; font-size: 40px; line-height: 1.05;
    text-transform: uppercase; letter-spacing: 2px; text-align: center;
    color: var(--ink);
  }
  .divider {
    position: absolute; left: 490px; top: 60px;
    width: 2px; height: 440px;
    background: linear-gradient(to bottom, transparent, var(--ink-soft) 15%, var(--ink) 70%, transparent);
  }
  .contact-side {
    flex: 1; padding: 90px 0 0 90px;
  }
  .person-name { font-weight: 700; font-size: 42px; line-height: 1; }
  .person-role { font-size: 16px; margin-top: 6px; padding-left: 90px; }
  .contact-list {
    list-style: none; margin-top: 70px;
    font-size: 30px; line-height: 1.55;
  }
</style>
</head>
<body>
<main class="canvas">
  <section class="business-card">
    <div class="brand-side">
      <div class="logo-artwork" role="img" aria-label="Logo illustration area: dove with olive branch over a globe, in blue line art"></div>
      <p class="brand-name">Harbor Lantern<br>Productions</p>
    </div>
    <div class="divider"></div>
    <div class="contact-side">
      <h1 class="person-name">Employee name</h1>
      <p class="person-role">Managing Director</p>
      <ul class="contact-list">
        <li>+61 478 315 064</li>
        <li>www.harborlantern.example</li>
        <li>teodor@harborlantern.example</li>
      </ul>
    </div>
  </section>
</main>
</body>
</html>
```